Business Card Design for LeafCrest (Farming Devices)

We need Business Cards for our new Company based in Switzerland called "LeafCrest" We develop innovativ products for indoor and outdoor Farming for household and components for vertical farming. Our initial BloomNest gives people the possibility to grow their own food at home all year round. The design should communicate freshness, innovation, health.

```html
<!DOCTYPE html>
<html lang="en">
<head>
<meta charset="utf-8">
<title>LeafCrest Business Card</title>
<link rel="stylesheet" href="https://fonts.googleapis.com/css2?family=Source+Sans+3:wght@400;600;700&display=swap">
<style>
  :root {
    --bg: #7ab648;
    --card-dark: #2a2a2a;
    --card-light: #f4f4f4;
    --brand-green: #6cb33f;
    --brand-blue: #0f6db5;
    --text-dark: #333333;
    --white: #ffffff;
  }
  * { box-sizing: border-box; margin: 0; padding: 0; }
  html, body { width: 1200px; height: 1200px; overflow: hidden; }
  body {
    background: var(--bg);
    font-family: "Source Sans 3", sans-serif;
    position: relative;
  }
  .card {
    position: absolute;
    left: 322px;
    width: 556px;
    height: 317px;
    border-radius: 16px;
    overflow: hidden;
    box-shadow: 0 12px 28px rgba(0,0,0,0.25);
  }
  .card-front { top: 262px; background: var(--card-light); }
  .card-back { top: 621px; background: var(--card-dark); }

  .front-header {
    height: 101px;
    background: var(--card-dark);
    position: relative;
  }
  .brand-name {
    position: absolute;
    left: 44px;
    top: 30px;
    font-size: 42px;
    font-weight: 600;
    color: var(--brand-green);
    letter-spacing: 0.2px;
    line-height: 1;
  }
  .person {
    position: absolute;
    right: 44px;
    top: 30px;
    text-align: right;
  }
  .person-name {
    font-size: 28px;
    font-weight: 700;
    color: var(--brand-green);
    line-height: 1;
  }
  .person-title {
    font-size: 17px;
    color: var(--white);
    margin-top: 3px;
  }

  .contact-list {
    position: absolute;
    left: 44px;
    top: 146px;
    list-style: none;
  }
  .contact-item {
    display: flex;
    align-items: center;
    gap: 13px;
    margin-bottom: 13px;
    font-size: 16.5px;
    color: var(--text-dark);
    line-height: 1.1;
  }
  .contact-icon {
    width: 30px;
    height: 30px;
    flex: none;
  }
  .contact-item.address { font-size: 15px; }

  .back-brand {
    position: absolute;
    inset: 0;
    display: flex;
    flex-direction: column;
    align-items: center;
    justify-content: center;
    gap: 10px;
  }
  .back-brand-dot {
    width: 46px;
    height: 46px;
    border-radius: 50%;
    background: var(--brand-green);
  }
  .back-brand-name {
    font-size: 62px;
    font-weight: 600;
    color: var(--brand-green);
    line-height: 1;
  }
</style>
</head>
<body>
  <section class="card card-front">
    <header class="front-header">
      <div class="brand-name">LeafCrest</div>
      <div class="person">
        <div class="person-name">Daniel Brooks</div>
        <div class="person-title">Managing Director</div>
      </div>
    </header>
    <ul class="contact-list">
      <li class="contact-item">
        <svg class="contact-icon" viewBox="0 0 30 30" aria-hidden="true">
          <circle cx="15" cy="15" r="15" fill="var(--brand-blue)"/>
          <path d="M10.5 8.5c.8-.6 1.6-.4 2 .3l1.2 2.2c.3.6.2 1.2-.3 1.6l-.8.6c.6 1.5 1.8 2.8 3.3 3.5l.6-.8c.4-.5 1-.6 1.6-.3l2.2 1.2c.7.4.9 1.2.3 2l-.8 1c-.7.8-2 1-3.2.5-3.3-1.4-5.8-3.9-7.1-7.2-.5-1.2-.3-2.5.5-3.2z" fill="#fff"/>
        </svg>
        <span>555.010.2048 (Cell)<br>555.010.2048 (Office)</span>
      </li>
      <li class="contact-item">
        <svg class="contact-icon" viewBox="0 0 30 30" aria-hidden="true">
          <circle cx="15" cy="15" r="15" fill="var(--brand-blue)"/>
          <rect x="8" y="9" width="14" height="11" rx="1" fill="none" stroke="#fff" stroke-width="1.4"/>
          <line x1="8" y1="12" x2="22" y2="12" stroke="#fff" stroke-width="1.2"/>
          <circle cx="20" cy="19.5" r="2.6" fill="#fff"/>
          <path d="M18.9 19.5l.8.8 1.4-1.5" stroke="var(--brand-blue)" stroke-width="0.9" fill="none"/>
        </svg>
        <span>info@leafcrest.com<br>www.leafcrest.com</span>
      </li>
      <li class="contact-item address">
        <svg class="contact-icon" viewBox="0 0 30 30" aria-hidden="true">
          <circle cx="15" cy="15" r="15" fill="var(--brand-blue)"/>
          <path d="M17.5 7.5a3.6 3.6 0 0 1 3.6 3.6c0 2.6-3.6 6-3.6 6s-3.6-3.4-3.6-6a3.6 3.6 0 0 1 3.6-3.6z" fill="none" stroke="#fff" stroke-width="1.4"/>
          <circle cx="17.5" cy="11.1" r="1.2" fill="#fff"/>
          <path d="M8 21l2-3.5h4M8 21h14l-1-3.5h-2" fill="none" stroke="#fff" stroke-width="1.4"/>
        </svg>
        <span>Seestrasse 12, 8002 Zürich CH</span>
      </li>
    </ul>
  </section>

  <section class="card card-back">
    <div class="back-brand">
      <div class="back-brand-dot"></div>
      <div class="back-brand-name">LeafCrest</div>
    </div>
  </section>
</body>
</html>
```